Dental Business Card

I need Dental oriented business cards.
On the front side -
- on the first line, my name:
Dr Marlo Vintner
- on the second line (just underneath):
Doctor of Dental Medicine
- on the third line, or underneath that or in a corner, I would like the address and phone number:
5182 Ch. Birchfield
Montreal QC H2T 4B9
514-629-5074
- other than that i would maybe like a logo of a tooth, but i want it to be subtle and very basic!
- I would like the card to be preferably black or dark grey-ish with the writing in white
On the other side -
- 2-3 lines with the possibility to write the next appointment the box with the lines should be white, with the rest of the card being black

```html
<!DOCTYPE html>
<html lang="en">
<head>
<meta charset="UTF-8">
<title>Dr Marlo Vintner – Business Card</title>
<link href="https://fonts.googleapis.com/css2?family=Open+Sans:wght@400;600&display=swap" rel="stylesheet">
<style>
  :root {
    --backdrop: #f2f2f2;
    --card: #38383d;
    --ink-light: #ffffff;
    --ink-soft: #e6e6e8;
    --panel: #f4f4f6;
    --ink-dark: #2e2e33;
  }
  html, body {
    margin: 0;
    padding: 0;
    width: 1200px;
    height: 900px;
    overflow: hidden;
    background: var(--backdrop);
    font-family: "Open Sans", sans-serif;
  }
  .card {
    position: absolute;
    top: 282px;
    width: 521px;
    height: 335px;
    background: var(--card);
    color: var(--ink-light);
  }
  .card--front { left: 44px; }
  .card--back { left: 635px; }

  /* front */
  .brand-mark {
    position: absolute;
    left: 60px;
    top: 120px;
    width: 140px;
    text-align: center;
    font-size: 22px;
    font-weight: 600;
    line-height: 1.25;
    color: var(--ink-light);
  }
  .divider {
    position: absolute;
    width: 2px;
    background: var(--ink-light);
  }
  .card--front .divider { left: 212px; top: 71px; height: 175px; }
  .front-details {
    position: absolute;
    left: 238px;
    top: 125px;
  }
  .doctor-name {
    margin: 0;
    font-size: 21px;
    font-weight: 600;
    line-height: 26px;
    letter-spacing: 0.2px;
  }
  .doctor-title, .doctor-phone {
    margin: 0;
    font-size: 17px;
    font-weight: 400;
    line-height: 24px;
    color: var(--ink-soft);
  }
  .address {
    position: absolute;
    left: 0;
    right: 0;
    top: 293px;
    margin: 0;
    text-align: center;
    font-size: 17px;
    color: var(--ink-soft);
  }

  /* back */
  .back-header {
    position: absolute;
    left: 28px;
    top: 21px;
    height: 53px;
    display: flex;
    align-items: center;
  }
  .mini-mark {
    flex: none;
    width: 24px;
    height: 24px;
    border: 2px solid var(--ink-light);
    border-radius: 50%;
    box-sizing: border-box;
  }
  .back-header .header-divider {
    flex: none;
    width: 2px;
    height: 53px;
    margin: 0 10px 0 11px;
    background: var(--ink-light);
  }
  .back-name {
    margin: 0;
    font-size: 21px;
    font-weight: 600;
    white-space: nowrap;
  }
  .back-title {
    margin: 0 0 0 14px;
    font-size: 16px;
    color: var(--ink-soft);
    white-space: nowrap;
  }
  .appointment-panel {
    position: absolute;
    left: 25px;
    top: 95px;
    width: 471px;
    height: 174px;
    background: var(--panel);
    color: var(--ink-dark);
  }
  .write-line {
    position: absolute;
    left: 32px;
    width: 406px;
    height: 34px;
    border-bottom: 1.5px solid var(--ink-dark);
    font-size: 16px;
    line-height: 34px;
  }
  .write-line:nth-child(1) { top: 4px; }
  .write-line:nth-child(2) { top: 39px; }
  .write-line:nth-child(3) { top: 74px; }
  .write-line:nth-child(4) { top: 109px; }
  .reschedule-note {
    position: absolute;
    left: 0;
    right: 0;
    top: 276px;
    margin: 0;
    text-align: center;
    font-size: 14.5px;
    line-height: 21px;
    color: var(--ink-soft);
  }
</style>
</head>
<body>
  <section class="card card--front" aria-label="Card front">
    <div class="brand-mark">Vintner<br>Dental</div>
    <div class="divider"></div>
    <div class="front-details">
      <h1 class="doctor-name">Dr Marlo Vintner</h1>
      <p class="doctor-title">Doctor of Dental Medicine</p>
      <p class="doctor-phone">514-629-5074</p>
    </div>
    <p class="address">5182 Ch. Birchfield Montreal QC H2T 4B9</p>
  </section>

  <section class="card card--back" aria-label="Card back">
    <div class="back-header">
      <div class="mini-mark"></div>
      <div class="header-divider"></div>
      <p class="back-name">Dr Marlo Vintner</p>
      <p class="back-title">Doctor of Dental Medicine</p>
    </div>
    <div class="appointment-panel">
      <div class="write-line">Client Name:</div>
      <div class="write-line">Next Appointment:</div>
      <div class="write-line"></div>
      <div class="write-line"></div>
    </div>
    <p class="reschedule-note">If you are unable to keep your appoinment please contact us on<br>514-629-5074 to rearrange or cancel</p>
  </section>
</body>
</html>
```